Tamworth Logistics

Create a modern, simple, Elegant business card design for my business.

Services: Vexa Trucks, Transport, Contract Logistics,

Business

Include all details same as old card plus new website address: www.tamworthlogistics-demo.com.au

• Similar colors to Logo.

```html
<!DOCTYPE html>
<html lang="en">
<head>
<meta charset="utf-8">
<title>Tamworth Logistics – Business Card</title>
<link href="https://fonts.googleapis.com/css2?family=Arimo:wght@400;700&display=swap" rel="stylesheet">
<style>
  :root {
    --bg: #2b2d30;
    --blue-deep: #0b4f86;
    --blue: #1472b5;
    --blue-light: #2a9bd8;
    --grey: #c8ccd0;
    --grey-text: #6b6f74;
    --white: #ffffff;
    --font: "Arimo", Arial, sans-serif;
  }
  * { box-sizing: border-box; margin: 0; padding: 0; }
  html, body { width: 1200px; height: 950px; overflow: hidden; }
  body { background: var(--bg); font-family: var(--font); position: relative; }

  .card {
    position: absolute;
    width: 700px;
    height: 400px;
    border-radius: 22px;
    overflow: hidden;
  }

  /* Back side */
  .card-back {
    left: 80px; top: 60px;
    background: radial-gradient(ellipse at 50% 35%, var(--blue-light) 0%, var(--blue) 40%, var(--blue-deep) 100%);
    color: var(--white);
    text-align: center;
    padding-top: 105px;
  }
  .brand {
    display: inline-flex;
    align-items: center;
    gap: 10px;
    font-weight: 700;
    font-size: 34px;
    letter-spacing: 0.5px;
  }
  .brand-dot { width: 14px; height: 14px; border-radius: 50%; }
  .card-back .brand { color: var(--white); }
  .card-back .brand-dot { background: var(--white); }
  .services-title {
    margin-top: 26px;
    font-size: 22px;
    font-weight: 700;
    letter-spacing: 1px;
  }
  .services-list { list-style: none; margin-top: 8px; font-size: 16px; line-height: 1.35; }

  /* Front side */
  .card-front { left: 420px; top: 500px; background: var(--white); }
  .front-shapes { position: absolute; inset: 0; width: 700px; height: 400px; }
  .holder { position: absolute; left: 40px; top: 165px; color: var(--white); }
  .holder-name { font-size: 24px; font-weight: 700; letter-spacing: 0.5px; }
  .holder-role { font-size: 18px; margin-top: 4px; }
  .card-front .brand {
    position: absolute; right: 42px; top: 130px;
    color: var(--blue); font-size: 30px;
  }
  .card-front .brand-dot { background: var(--blue); }
  .contacts {
    position: absolute; right: 40px; top: 205px;
    list-style: none; text-align: right;
    color: var(--grey-text); font-size: 15px; line-height: 26px;
  }
  .contacts li { display: flex; justify-content: flex-end; align-items: center; gap: 10px; }
  .contact-icon {
    width: 16px; height: 16px; border-radius: 50%;
    background: var(--blue-deep);
    display: inline-flex; align-items: center; justify-content: center;
  }
  .contact-icon svg { width: 10px; height: 10px; }
</style>
</head>
<body>

<section class="card card-back">
  <div class="brand"><span class="brand-dot"></span>Tamworth Logistics</div>
  <h2 class="services-title">SERVICES</h2>
  <ul class="services-list">
    <li>Vexa Trucks</li>
    <li>All General &amp; Oversize Trasport</li>
    <li>Specialized Transport | Contract Logistics</li>
    <li>Express Hotshot Services</li>
  </ul>
</section>

<section class="card card-front">
  <svg class="front-shapes" viewBox="0 0 700 400" aria-hidden="true">
    <defs>
      <linearGradient id="frontBlue" x1="0" y1="0" x2="1" y2="1">
        <stop offset="0" stop-color="#0b4f86"/>
        <stop offset="0.55" stop-color="#1472b5"/>
        <stop offset="1" stop-color="#2a9bd8"/>
      </linearGradient>
    </defs>
    <path d="M0 0 H660 Q300 70 205 400 H0 Z" fill="#c8ccd0"/>
    <path d="M0 0 H632 Q280 64 186 400 H0 Z" fill="#ffffff"/>
    <path d="M0 0 H612 Q262 58 168 400 H0 Z" fill="url(#frontBlue)"/>
  </svg>

  <div class="holder">
    <p class="holder-name">ALEX MORGAN</p>
    <p class="holder-role">President</p>
  </div>

  <div class="brand"><span class="brand-dot"></span>Tamworth Logistics</div>

  <ul class="contacts">
    <li>0400 555 123
      <span class="contact-icon"><svg viewBox="0 0 10 10"><path d="M2 1 L4 1 L4.5 3 L3.5 3.8 Q4.5 5.8 6.2 6.5 L7 5.5 L9 6 L9 8 Q5 9 2 5 Q1 3 2 1Z" fill="#fff"/></svg></span>
    </li>
    <li>info@tamworthlogistics-demo.com.au
      <span class="contact-icon"><svg viewBox="0 0 10 10"><rect x="1" y="2.5" width="8" height="5.5" fill="#fff"/><path d="M1 2.5 L5 5.5 L9 2.5" stroke="#0b4f86" stroke-width="0.8" fill="none"/></svg></span>
    </li>
    <li>www.tamworthlogistics-demo.com.au
      <span class="contact-icon"><svg viewBox="0 0 10 10"><circle cx="5" cy="5" r="3.8" stroke="#fff" stroke-width="1" fill="none"/><path d="M1.2 5 H8.8 M5 1.2 V8.8" stroke="#fff" stroke-width="0.8"/></svg></span>
    </li>
  </ul>
</section>

</body>
</html>
```